QM Regulatory Pathways - Biz Card - Re-do

I would like a re-do on my business card.

See my Internet site - qmregpathways.example

1) Remove direct phone line.
2) Add company moto - integrity, diligence, and excellence
3) Add Consulting Services listing:
-Benefit Technology
-ERISA Compliance
-Contract/Vendor Management
-Human Resource/Payroll
-Medical/Prescription Drug
-Integrated Leave of Absence

Target Market(s)

Employee benefit consulting and insurance purchasers, Usually human resource executives

Industry/Entity Type

Human Resource

Contact Information for Business Card

Same business card color scheme, logo,

Font styles to use
Sans Serif

Requirements
Must have
• Same color scheme and logo. Remove direct phone number. Keep all numbers, internet address.

```html
<!DOCTYPE html>
<html lang="en">
<head>
<meta charset="utf-8">
<title>QM Regulatory Pathways – Business Card</title>
<link rel="stylesheet" href="https://fonts.googleapis.com/css2?family=Arimo:wght@700&family=Source+Sans+3:wght@400;600;700&display=swap">
<style>
  :root {
    --plum: #560a52;
    --paper: #f4f6f8;
    --ink: #111111;
    --white: #ffffff;
    --icon: #ece4ee;
    --page: #ffffff;
  }
  * { box-sizing: border-box; margin: 0; padding: 0; }
  html, body {
    width: 1200px; height: 1000px; overflow: hidden;
    background: var(--page);
    font-family: "Source Sans 3", "Helvetica Neue", Arial, sans-serif;
  }
  .canvas { position: relative; width: 1200px; height: 1000px; }

  .card {
    position: absolute; width: 731px; height: 429px;
    background: var(--paper); overflow: hidden;
  }
  .card--front { left: 134px; top: 46px; }
  .card--back  { left: 313px; top: 515px; }

  .band-top { position: absolute; left: 0; top: 0; width: 100%; height: 32px; background: var(--plum); }
  .panel { position: absolute; left: 0; width: 100%; background: var(--plum); color: var(--white); }
  .card--front .panel { top: 247px; height: 182px; }
  .card--back .panel  { top: 223px; height: 206px; }

  .accent-rule { position: absolute; left: 0; top: 0; }

  .brand-mark { position: absolute; border-radius: 50%; background: var(--plum); }
  .brand-name { position: absolute; color: var(--plum); font-weight: 400; white-space: nowrap; text-align: center; }

  .card--front .brand-mark { left: 50px; top: 50px; width: 142px; height: 142px; }
  .card--front .brand-name { left: 0; width: 250px; top: 197px; font-size: 20px; }

  .holder { position: absolute; left: 380px; width: 292px; top: 58px; text-align: center; font-family: "Arimo", Arial, sans-serif; font-weight: 700; }
  .holder__name { font-size: 34px; color: var(--plum); text-decoration: underline; text-decoration-thickness: 3px; text-underline-offset: 4px; line-height: 1.1; }
  .holder__title { font-size: 29px; color: var(--ink); margin-top: 4px; }

  .contact { position: absolute; top: 0; text-align: center; }
  .contact svg { display: block; }
  .contact--phone { left: 27px; width: 160px; }
  .contact--phone .icons { position: absolute; left: 58px; top: 27px; }
  .contact--phone .lines { position: absolute; left: 0; top: 74px; text-align: left; font-size: 16px; font-weight: 600; line-height: 22px; white-space: pre; }

  .contact--web { left: 200px; width: 330px; }
  .contact--web .icons { position: absolute; left: 122px; top: 30px; display: flex; gap: 20px; }
  .contact--web .email { position: absolute; left: 0; width: 100%; top: 72px; font-size: 18px; }
  .contact--web .site { position: absolute; left: 0; width: 100%; top: 98px; font-size: 25px; font-weight: 700; }

  .contact--address { left: 540px; width: 170px; }
  .contact--address .icons { position: absolute; left: 71px; top: 22px; }
  .contact--address .lines { position: absolute; left: 0; width: 100%; top: 74px; font-size: 14.5px; line-height: 20px; }

  .card--back .brand-mark { left: 327px; top: 50px; width: 80px; height: 80px; }
  .card--back .brand-name { left: 0; width: 100%; top: 130px; font-size: 38px; }

  .services { position: absolute; left: 52px; top: 22px; width: 660px; }
  .services__heading { font-size: 23px; font-weight: 700; text-decoration: underline; text-underline-offset: 4px; }
  .services__list { position: absolute; top: 50px; list-style: none; font-size: 22px; line-height: 27px; white-space: nowrap; }
  .services__list li::before { content: ". "; }
  .services__list--left { left: 0; }
  .services__list--right { left: 325px; top: 47px; }
</style>
</head>
<body>
<div class="canvas">

  <section class="card card--front" aria-label="Business card front">
    <div class="band-top"></div>
    <svg class="accent-rule" width="731" height="429" aria-hidden="true">
      <polygon points="326,247 344,223 731,223 731,229 349,229 335,247" fill="var(--plum)"/>
    </svg>
    <div class="brand-mark"></div>
    <div class="brand-name">QM Regulatory Pathways</div>

    <div class="holder">
      <div class="holder__name">Daniel Whitford</div>
      <div class="holder__title">President</div>
    </div>

    <div class="panel">
      <div class="contact contact--phone">
        <div class="icons">
          <svg width="32" height="32" viewBox="0 0 24 24" aria-hidden="true"><path fill="var(--icon)" d="M6.6 10.8a15.1 15.1 0 0 0 6.6 6.6l2.2-2.2c.3-.3.7-.4 1-.2 1.1.4 2.3.6 3.6.6.6 0 1 .4 1 1V20c0 .6-.4 1-1 1C10.6 21 3 13.4 3 4c0-.6.4-1 1-1h3.5c.6 0 1 .4 1 1 0 1.3.2 2.5.6 3.6.1.3 0 .7-.2 1z"/></svg>
        </div>
        <div class="lines">Main : 555.210.4400
Fax   : 555.210.4401</div>
      </div>

      <div class="contact contact--web">
        <div class="icons">
          <svg width="34" height="28" viewBox="0 0 34 28" aria-hidden="true"><rect x="1" y="2" width="32" height="24" rx="3" fill="var(--icon)"/><path d="M4 6 L17 16 L30 6" fill="none" stroke="var(--plum)" stroke-width="2.5"/></svg>
          <svg width="32" height="32" viewBox="0 0 32 32" aria-hidden="true"><circle cx="16" cy="16" r="15" fill="var(--icon)"/><circle cx="16" cy="16" r="11" fill="none" stroke="var(--plum)" stroke-width="2"/><path d="M16 5v22M5 16h22M16 5c-5 5-5 17 0 22M16 5c5 5 5 17 0 22" fill="none" stroke="var(--plum)" stroke-width="2"/></svg>
        </div>
        <div class="email">dwhitford@qmregpathways.example</div>
        <div class="site">qmregpathways.example</div>
      </div>

      <div class="contact contact--address">
        <div class="icons">
          <svg width="28" height="38" viewBox="0 0 24 32" aria-hidden="true"><path fill="var(--icon)" d="M12 0C5.4 0 0 5.3 0 11.9 0 20.8 12 32 12 32s12-11.2 12-20.1C24 5.3 18.6 0 12 0z"/><circle cx="12" cy="11.5" r="4.5" fill="var(--plum)"/></svg>
        </div>
        <div class="lines">Harbor Street NW, 180<br>Suite 300 Lakeview,<br>MI 49000</div>
      </div>
    </div>
  </section>

  <section class="card card--back" aria-label="Business card back">
    <div class="band-top"></div>
    <div class="brand-mark"></div>
    <div class="brand-name">QM Regulatory Pathways</div>

    <div class="panel">
      <div class="services">
        <div class="services__heading">Consulting Services listing</div>
        <ul class="services__list services__list--left">
          <li>ERISA Compliance</li>
          <li>Benefit Technology</li>
          <li>Human Resource/Payroll</li>
        </ul>
        <ul class="services__list services__list--right">
          <li>Medical/Prescription Drug</li>
          <li>Integrated Leave of Absence</li>
          <li>Contract/Vendor Management</li>
        </ul>
      </div>
    </div>
  </section>

</div>
</body>
</html>
```